Lantern Hearthworks Business Cards

Looking to create simple business cards that highlight our unique three sided triangle fire pit design with the colors and font of our logo, listed below.

Colors

Designer to choose colors to be used in the design.

Requirements
Must have
• Looking for something simple that includes a picture of our fire pit with name, website (lanternhearthworks.com), phone number and email. Want to keep the color mostly orange and black.
• Font is gotham(medium) and orange color code is #ee6e22

```html
<!DOCTYPE html>
<html lang="en">
<head>
<meta charset="utf-8">
<title>Lantern Hearthworks Business Cards</title>
<link rel="stylesheet" href="https://fonts.googleapis.com/css2?family=Montserrat:wght@400;500&display=swap">
<style>
  :root {
    --orange: #ee6e22;
    --black: #0c0c0c;
    --stone: #3c3c3c;
    --stone-dark: #1c1c1c;
    --white: #f2f2f2;
    --grey: #d0d0d0;
    --backdrop: #e4e4e2;
  }
  * { box-sizing: border-box; margin: 0; padding: 0; }
  html, body {
    width: 1200px; height: 1021px; overflow: hidden;
    background: var(--backdrop);
    font-family: "Montserrat", sans-serif;
  }
  .sheet {
    width: 1200px; height: 1021px;
    display: flex; align-items: center; justify-content: center; gap: 70px;
  }
  .card {
    position: relative; width: 380px; height: 665px; overflow: hidden;
    box-shadow: 0 10px 28px rgba(0,0,0,.25);
  }
  .accent-bar { position: absolute; height: 14px; background: var(--orange); }
  .accent-bar--top { top: 22px; left: 60px; width: 250px; }
  .accent-bar--bottom { bottom: 22px; left: 70px; width: 250px; }

  .wordmark {
    position: absolute; left: 0; right: 0;
    display: flex; align-items: center; justify-content: center; gap: 14px;
    color: var(--white); font-weight: 500; text-transform: uppercase;
    font-size: 27px; letter-spacing: 5px; line-height: 1.15;
  }
  .wordmark-mark { width: 14px; height: 14px; background: var(--orange); flex: none; }
  .wordmark-text { display: flex; flex-direction: column; }

  /* front */
  .card--front .firepit-photo {
    position: absolute; inset: 0;
    background:
      radial-gradient(circle at 48% 40%, rgba(255,170,70,.95) 0%, rgba(238,110,34,.85) 14%, rgba(120,50,15,.45) 28%, rgba(60,60,60,0) 42%),
      radial-gradient(ellipse at 50% 45%, #4a4a4a 0%, var(--stone) 50%, var(--stone-dark) 100%);
  }
  .card--front .wordmark { top: 470px; }

  /* back */
  .card--back { background: var(--black); }
  .contact { position: absolute; top: 100px; left: 0; right: 0; text-align: center; }
  .contact-name { color: var(--orange); font-weight: 500; font-size: 22px; }
  .contact-role { color: var(--grey); font-weight: 400; font-size: 16px; margin-top: 2px; }
  .contact-icons { display: flex; justify-content: center; gap: 10px; margin-top: 44px; }
  .contact-icons svg { width: 14px; height: 14px; }
  .contact-list { list-style: none; margin-top: 8px; color: var(--white); font-size: 16px; line-height: 1.45; }
  .card--back .wordmark { top: 520px; font-size: 28px; }
</style>
</head>
<body>
<main class="sheet">
  <section class="card card--front">
    <div class="firepit-photo" role="img" aria-label="Photograph of a triangular steel fire pit with burning logs on dark gravel"></div>
    <div class="accent-bar accent-bar--top"></div>
    <div class="wordmark"><span class="wordmark-mark"></span><span class="wordmark-text"><span>Lantern</span><span>Hearthworks</span></span></div>
    <div class="accent-bar accent-bar--bottom"></div>
  </section>

  <section class="card card--back">
    <div class="accent-bar accent-bar--top"></div>
    <div class="contact">
      <p class="contact-name">Evan Marlowe</p>
      <p class="contact-role">Co-Founder</p>
      <div class="contact-icons">
        <svg viewBox="0 0 16 16" aria-hidden="true"><path d="M4 1l3 3-2 2c1 2 3 4 5 5l2-2 3 3-2 3C7 14 2 9 1 3z" fill="#ee6e22"/></svg>
        <svg viewBox="0 0 16 16" aria-hidden="true"><rect x="1.5" y="3.5" width="13" height="9" fill="none" stroke="#ee6e22" stroke-width="1.5"/><path d="M1.5 3.5l6.5 5 6.5-5" fill="none" stroke="#ee6e22" stroke-width="1.5"/></svg>
        <svg viewBox="0 0 16 16" aria-hidden="true"><circle cx="8" cy="8" r="6.5" fill="none" stroke="#ee6e22" stroke-width="1.5"/><ellipse cx="8" cy="8" rx="3" ry="6.5" fill="none" stroke="#ee6e22" stroke-width="1.2"/><path d="M1.5 8h13" stroke="#ee6e22" stroke-width="1.2"/></svg>
      </div>
      <ul class="contact-list">
        <li>555-014-2937</li>
        <li>lanternhearthworks@mail.com</li>
        <li>lanternhearthworks.com</li>
      </ul>
    </div>
    <div class="wordmark"><span class="wordmark-mark"></span><span class="wordmark-text"><span>Lantern</span><span>Hearthworks</span></span></div>
    <div class="accent-bar accent-bar--bottom"></div>
  </section>
</main>
</body>
</html>
```